Pine Ridge Dwellings Stationary and Simplified Embroidery Contest
Business Card, Letterhead, Envelope, Note Pad, Sticker, Embroidery
Pine Ridge Dwellings Stationary and Simplified Embroidery Contest -
Creative Brief
Professional
Wendell Marsh
Construction Manager
4812 Galloway Street Edmonton AB T5K 3R8
wendell@pineridgedwellings.example
www.pineridgedwellings.example
Please include some with light backgrounds as well as dark options... we want to be able to print a few cards so that not every card we hand out is the same! I would like to have 4-6 business card designs. The embroidery part would just be a simplified logo.
Comments/Blank space for notes to written on the business card. We have looked at a few designs for business cards and like the Logo and Name on the front with all the details on the back, but do be creative with this is by no means a rule!

```html
<!DOCTYPE html>
<html lang="en">
<head>
<meta charset="utf-8">
<title>Pine Ridge Dwellings Stationery</title>
<link href="https://fonts.googleapis.com/css2?family=Cinzel:wght@600&family=Open+Sans:wght@400;600&display=swap" rel="stylesheet">
<style>
  :root{
    --backdrop:#d9c9ad;
    --paper:#ffffff;
    --accent:#e8951c;
    --forest:#5f6b4b;
    --charcoal:#333333;
    --ink:#555555;
    --rule:#bdbdbd;
    --label:#2b2b2b;
  }
  *{box-sizing:border-box;margin:0;padding:0}
  html,body{width:1200px;height:749px;overflow:hidden}
  body{background:var(--backdrop);font-family:"Open Sans",Arial,sans-serif;color:var(--ink);position:relative}
  .item{position:absolute}
  .label{position:absolute;font-size:6px;font-weight:600;color:var(--label);text-align:center;width:100%;top:-10px;white-space:nowrap}
  .paper{background:var(--paper);box-shadow:0 2px 5px rgba(0,0,0,.35)}

  .brand{display:flex;flex-direction:column;align-items:center;gap:2px}
  .brand-dot{border-radius:50%;background:var(--accent);width:18px;height:18px}
  .brand-name{font-family:"Cinzel",Georgia,serif;font-weight:600;color:var(--charcoal);font-size:7px;letter-spacing:.3px;white-space:nowrap}

  /* sheets */
  .sheet{width:269px;height:389px;top:343px}
  .sheet .brand{position:absolute;top:14px;left:0;right:0}
  .sheet-foot{position:absolute;left:0;right:0;bottom:0}
  .sheet-foot p{font-size:4.5px;text-align:center;padding-bottom:3px;color:var(--ink)}
  .sheet-foot .band{height:6px;background:var(--accent)}
  .fax-title{position:absolute;right:22px;top:58px;font-size:7px;font-weight:600;color:var(--charcoal)}
  .fax-table{position:absolute;left:20px;top:67px;border-collapse:collapse;font-size:5px;width:229px}
  .fax-table td{border:1px solid var(--rule);height:14px;padding-left:3px}
  .fax-table td.key{width:30px;background:#f4f4f4}
  .fax-checks{position:absolute;left:20px;top:134px;display:flex;gap:12px;font-size:5px;white-space:nowrap}
  .fax-checks span::before{content:"";display:inline-block;width:5px;height:5px;border:1px solid var(--ink);margin-right:2px;vertical-align:-1px}

  /* cards */
  .card{width:62px;height:58px;overflow:hidden}
  .card .band{position:absolute;left:0;right:0;bottom:0;height:6px;background:var(--charcoal)}
  .card .band::before{content:"";position:absolute;left:0;top:0;width:40%;height:2px;background:var(--accent)}
  .card-front .brand{position:absolute;left:0;right:0;top:12px}
  .card-front .brand-dot{width:16px;height:16px}
  .card-front .brand-name{font-size:4.2px;letter-spacing:0}
  .card-back .details{position:absolute;left:4px;top:4px;font-size:3.2px;line-height:1.45;white-space:nowrap}
  .card-back .details strong{font-size:4.5px;color:var(--charcoal);display:block}
  .card-back .notes{position:absolute;left:4px;right:4px;top:36px;height:13px;border:1px solid var(--rule);font-size:3.2px;padding:1px 2px}

  /* envelopes */
  .envelope{width:305px;height:139px}
  .envelope .band{position:absolute;left:0;right:0;bottom:0;height:5px;background:var(--accent)}
  .envelope .return{position:absolute;left:10px;top:10px;display:flex;gap:6px;align-items:flex-start}
  .envelope .return p{font-size:4.5px;line-height:1.5}
  .flap-envelope{width:312px}
  .flap-envelope svg{position:absolute;left:0;top:0}
  .flap-envelope .brand{position:absolute;left:0;right:0}
  .flap-envelope .brand-name{color:#fff;font-size:6px}
</style>
</head>
<body>

<!-- business cards -->
<div class="item paper card card-front" style="left:283px;top:180px">
  <span class="label">Card Option 1 (Front)</span>
  <div class="brand"><span class="brand-dot"></span><span class="brand-name">Pine Ridge Dwellings</span></div>
  <div class="band"></div>
</div>
<div class="item paper card card-back" style="left:352px;top:180px">
  <span class="label">Card Option 1 (Back)</span>
  <div class="details"><strong>Wendell Marsh</strong>Construction Manager<br>4812 Galloway Street<br>Edmonton AB T5K 3R8<br>www.pineridgedwellings.example</div>
  <div class="notes">Notes</div>
  <div class="band"></div>
</div>
<div class="item paper card card-front" style="left:283px;top:256px;background:var(--charcoal)">
  <span class="label">Card Option 2 (Front)</span>
  <div class="brand"><span class="brand-dot"></span><span class="brand-name" style="color:#fff">Pine Ridge Dwellings</span></div>
</div>
<div class="item paper card card-back" style="left:352px;top:256px">
  <span class="label">Card Option 2 (Back)</span>
  <div class="details"><strong>Wendell Marsh</strong>Construction Manager<br>wendell@pineridgedwellings.example<br>4812 Galloway Street<br>Edmonton AB T5K 3R8</div>
  <div class="notes">Notes</div>
  <div class="band"></div>
</div>

<!-- flat envelopes -->
<div class="item paper envelope" style="left:499px;top:19px">
  <span class="label">Envelope (Front)</span>
  <div class="return"><div class="brand"><span class="brand-dot"></span><span class="brand-name">Pine Ridge Dwellings</span></div>
  <p>4812 Galloway Street<br>Edmonton AB<br>T5K 3R8</p></div>
  <div class="band"></div>
</div>
<div class="item paper envelope" style="left:499px;top:173px">
  <span class="label">Envelope (Back)</span>
  <div class="band"></div>
</div>

<!-- flap envelopes -->
<div class="item paper envelope flap-envelope" style="left:876px;top:29px;height:95px">
  <span class="label">Envelope Option 1 (Back)</span>
  <svg width="312" height="95"><polyline points="0,0 156,55 312,0" fill="none" stroke="#cfcfcf"/></svg>
</div>
<div class="item paper envelope flap-envelope" style="left:876px;top:95px;height:90px">
  <svg width="312" height="90"><polygon points="0,0 312,0 156,60" fill="var(--forest)"/></svg>
  <div class="brand" style="top:22px"><span class="brand-dot" style="width:12px;height:12px"></span><span class="brand-name">Pine Ridge Dwellings</span></div>
</div>
<div class="item paper envelope flap-envelope" style="left:876px;top:172px;height:143px">
  <svg width="312" height="143"><polygon points="0,0 312,0 156,75" fill="var(--accent)"/></svg>
  <div class="brand" style="top:30px"><span class="brand-dot" style="width:14px;height:14px;background:var(--charcoal)"></span><span class="brand-name" style="color:var(--charcoal)">Pine Ridge Dwellings</span></div>
</div>

<!-- sheets -->
<div class="item paper sheet" style="left:24px">
  <span class="label">Fax Sheet</span>
  <div class="brand"><span class="brand-dot"></span><span class="brand-name">Pine Ridge Dwellings</span></div>
  <div class="fax-title">FAX</div>
  <table class="fax-table">
    <tr><td class="key">To:</td><td></td><td class="key">From:</td><td></td></tr>
    <tr><td class="key">Fax:</td><td></td><td class="key">Pages:</td><td></td></tr>
    <tr><td class="key">Phone:</td><td></td><td class="key">Date:</td><td></td></tr>
    <tr><td class="key">Re:</td><td></td><td class="key">CC:</td><td></td></tr>
  </table>
  <div class="fax-checks"><span>Urgent</span><span>For Review</span><span>Please Comment</span><span>Please Reply</span></div>
  <div class="sheet-foot"><p>4812 Galloway Street Edmonton AB T5K 3R8 · www.pineridgedwellings.example</p><div class="band"></div></div>
</div>

<div class="item paper sheet" style="left:312px">
  <span class="label">Letterhead</span>
  <div class="brand"><span class="brand-dot"></span><span class="brand-name">Pine Ridge Dwellings</span></div>
  <div class="sheet-foot"><p>4812 Galloway Street Edmonton AB T5K 3R8 · www.pineridgedwellings.example</p><div class="band"></div></div>
</div>

<div class="item paper sheet" style="left:607px">
  <span class="label">Fax Sheet</span>
  <div class="brand"><span class="brand-dot"></span><span class="brand-name">Pine Ridge Dwellings</span></div>
  <div class="fax-title">FAX</div>
  <table class="fax-table">
    <tr><td class="key">To:</td><td></td><td class="key">From:</td><td></td></tr>
    <tr><td class="key">Fax:</td><td></td><td class="key">Pages:</td><td></td></tr>
    <tr><td class="key">Phone:</td><td></td><td class="key">Date:</td><td></td></tr>
    <tr><td class="key">Re:</td><td></td><td class="key">CC:</td><td></td></tr>
  </table>
  <div class="fax-checks"><span>Urgent</span><span>For Review</span><span>Please Comment</span><span>Please Reply</span></div>
  <div class="sheet-foot"><p>4812 Galloway Street Edmonton AB T5K 3R8 · www.pineridgedwellings.example</p><div class="band"></div></div>
</div>

<div class="item paper sheet" style="left:895px">
  <span class="label">Letterhead</span>
  <div class="brand"><span class="brand-dot"></span><span class="brand-name">Pine Ridge Dwellings</span></div>
  <div class="sheet-foot"><p>4812 Galloway Street Edmonton AB T5K 3R8 · www.pineridgedwellings.example</p><div class="band"></div></div>
</div>

</body>
</html>
```